Website for Vayu Kiran Holdings

Need a project marketing website for our company which primarily deals in selling real estate(land sales) from Big Estates to Builders /Clients, help them in Building & Construction and do all Project Management.

Coding

Coded - Design and coding required

Number of Pages Required

4 page

Colors
0054AA
0677BA
7BADD7
CADEEF
E8F1F8
FFC000
F8CF3A
FAE287
FDF2CF
FEFAEE

```html
<!DOCTYPE html>
<html lang="en">
<head>
<meta charset="utf-8">
<title>Vayu Kiran Holdings</title>
<link href="https://fonts.googleapis.com/css2?family=Poppins:wght@300;400;500;600;700&family=Josefin+Sans:wght@400;500;600&display=swap" rel="stylesheet">
<style>
:root{
  --blue:#0054AA;
  --blue-mid:#0677BA;
  --blue-soft:#7BADD7;
  --blue-pale:#CADEEF;
  --blue-mist:#E8F1F8;
  --gold:#FFC000;
  --gold-soft:#F8CF3A;
  --ink:#16233a;
  --text:#2b2b2b;
  --panel:#3a7cc7;
  --footer:#131313;
}
*{margin:0;padding:0;box-sizing:border-box}
html,body{width:1200px;height:3022px;overflow:hidden}
body{position:relative;background:#fff;font-family:'Poppins',sans-serif;color:var(--text)}
.abs{position:absolute}
a{color:inherit;text-decoration:none}

/* header */
.site-header{position:absolute;left:0;top:0;width:1200px;height:88px;background:#fff}
.brand{position:absolute;left:115px;top:14px;font-weight:600;color:var(--ink);font-size:25px;line-height:30px;letter-spacing:-.3px}
.brand span{display:block;font-size:20px;line-height:28px}
.nav a{position:absolute;top:35px;font-size:14px;color:#222}
.nav a.active{color:var(--blue-mid);font-weight:500}
.nav a.active::before{content:"";position:absolute;left:50%;top:-7px;width:10px;height:2px;margin-left:-5px;background:var(--blue-mid)}
.btn-contact{position:absolute;left:737px;top:20px;width:140px;height:47px;border-radius:6px;background:var(--blue);color:#fff;font-weight:600;font-size:14px;display:flex;align-items:center;justify-content:center}
.agent-icon{position:absolute;left:900px;top:26px;width:38px;height:38px;border:1.5px solid var(--blue);border-radius:50%;display:flex;align-items:center;justify-content:center}
.agent-label{position:absolute;left:951px;top:24px;font-size:11px;letter-spacing:2.4px;color:#555;font-weight:500}
.agent-phone{position:absolute;left:951px;top:39px;font-size:21px;font-weight:600;color:var(--ink)}

/* hero */
.hero{position:absolute;left:0;top:88px;width:1200px;height:624px;background:linear-gradient(100deg,#3d77b4 0%,#4f8cc4 35%,#7aa9d4 60%,#9dbfdc 85%,#8fa9c4 100%)}
.hero-title{position:absolute;left:118px;top:222px;color:#fff;font-size:48px;line-height:54px;font-weight:300}
.hero-title b{font-weight:700;display:block}
.hero-copy{position:absolute;left:118px;top:339px;width:480px;color:#fff;font-size:17px;line-height:23px}
.btn-gold{position:absolute;left:118px;top:402px;width:125px;height:47px;border-radius:6px;background:var(--gold);color:#fff;font-weight:600;font-size:14px;display:flex;align-items:center;justify-content:center}
.btn-ghost{position:absolute;left:264px;top:402px;width:148px;height:47px;border-radius:6px;border:2px solid #fff;color:#fff;font-weight:600;font-size:14px;display:flex;align-items:center;justify-content:center}
.dot{position:absolute;top:631px;width:14px;height:14px;border-radius:50%;border:1.5px solid #fff}
.dot.on{background:var(--gold);border-color:var(--gold)}

/* about */
.wave{position:absolute;left:0;top:1080px;width:1200px;height:320px;background:linear-gradient(180deg,#fff 0%,#f1f3f6 45%,#fff 100%)}
.photo-a{position:absolute;left:81px;top:816px;width:303px;height:393px;border-radius:14px;background:linear-gradient(160deg,#c58a4b,#8a6a50 55%,#6a5b52)}
.photo-b{position:absolute;left:273px;top:942px;width:310px;height:358px;border-radius:14px;border:8px solid #fff;background:linear-gradient(120deg,#c8ccd2,#e6e6e6 45%,#3a3d44);box-shadow:0 6px 20px rgba(0,0,0,.08)}
.section-title{font-size:35px;font-weight:300;color:var(--ink)}
.section-title b{font-weight:700}
.rule{position:absolute;height:2px;background:var(--blue-mid)}
.about-title{position:absolute;left:603px;top:841px}
.about-text{position:absolute;left:603px;width:475px;font-family:'Josefin Sans',sans-serif;font-size:16px;line-height:25.8px;color:#222}
.about-text.lead{top:920px;font-weight:600}
.about-text.more{top:1067px}
.btn-learn{position:absolute;left:603px;top:1203px;width:150px;height:47px;border-radius:4px;background:var(--blue);color:#fff;font-weight:600;font-size:14px;display:flex;align-items:center;justify-content:center}

/* services */
.services-title{position:absolute;left:0;width:1200px;top:1380px;text-align:center}
.card{position:absolute;top:1477px;width:281px;height:361px;border-radius:20px;background:var(--blue);color:#fff;padding:0 20px}
.card svg{position:absolute;left:20px;top:48px}
.card h3{position:absolute;left:20px;top:156px;font-size:20px;font-weight:600}
.card .bar{position:absolute;left:20px;top:189px;width:52px;height:2px;background:#fff}
.card p{position:absolute;left:20px;top:205px;width:240px;font-family:'Josefin Sans',sans-serif;font-size:12.5px;line-height:18px}
.card.feature{background:var(--gold);color:var(--ink);border:5px solid #111;box-shadow:0 10px 18px rgba(0,0,0,.25)}
.card.feature .bar{background:var(--ink)}
.card.feature svg{left:15px}
.card.feature h3,.card.feature .bar,.card.feature p{left:15px}
.card.feature .more{position:absolute;left:15px;top:322px;font-size:11px;text-decoration:underline}

/* contact */
.contact-title{position:absolute;left:0;width:1200px;top:1930px;text-align:center}
.contact-sub{position:absolute;left:0;width:1200px;top:2013px;text-align:center;font-family:'Josefin Sans',sans-serif;font-size:21px;font-weight:500;color:var(--ink)}
.landscape{position:absolute;left:0;top:2330px;width:1200px;height:282px;background:linear-gradient(180deg,#fff 0%,#dde3e3 30%,#8e9c86 65%,#6f7f63 100%)}
.contact-card{position:absolute;left:156px;top:2079px;width:888px;height:391px;border-radius:32px;background:#fff;box-shadow:0 8px 24px rgba(0,0,0,.12);overflow:hidden}
.info-panel{position:absolute;left:534px;top:0;width:354px;height:391px;background:var(--panel);border-radius:32px 32px 0 0;color:#fff}
.form-title{position:absolute;left:21px;top:18px;font-size:21px;font-weight:500;color:var(--ink)}
.field{position:absolute;width:219px;border-bottom:1.5px solid var(--blue-soft);height:42px}
.field label{display:block;font-size:11px;color:#666;line-height:14px}
.field span{display:block;font-size:13px;color:#222;margin-top:5px}
.field.msg{width:398px;height:118px}
.send{position:absolute;left:437px;top:274px;width:66px;height:66px;border-radius:50%;background:#222;display:flex;align-items:center;justify-content:center}
.info-title{position:absolute;left:30px;top:22px;font-size:22px;font-weight:500}
.info-row{position:absolute;left:81px;font-size:16px;font-weight:500;line-height:23px}
.info-icon{position:absolute;left:29px}
.social{position:absolute;top:271px;width:28px;height:28px;border-radius:50%;border:1.5px solid #fff;background:rgba(255,255,255,.15)}
.social.solid{background:#fff}

/* footer */
.site-footer{position:absolute;left:0;top:2612px;width:1200px;height:410px;background:var(--footer);color:#fff}
.footer-brand{position:absolute;left:190px;top:130px;font-size:40px;font-weight:600;line-height:46px}
.footer-brand span{display:block;font-size:30px;line-height:38px}
.fcol{position:absolute;top:88px}
.fcol h4{font-size:20px;font-weight:600}
.fcol .bar{width:66px;height:3px;background:var(--gold);margin:5px 0 12px}
.fcol a{display:block;font-size:13px;line-height:26px}
.footer-rule{position:absolute;left:111px;top:299px;width:978px;height:1px;background:#4a3f18}
.copy{position:absolute;top:334px;font-size:13px}
</style>
</head>
<body>

<header class="site-header">
  <div class="brand">VAYU KIRAN<span>HOLDINGS</span></div>
  <nav class="nav">
    <a class="active" style="left:457px">Home</a>
    <a style="left:528px">About</a>
    <a style="left:598px">Services</a>
    <a style="left:681px">Blog</a>
  </nav>
  <a class="btn-contact">CONTACT US</a>
  <div class="agent-icon">
    <svg width="18" height="18" viewBox="0 0 24 24"><path d="M6.6 10.8a15.1 15.1 0 0 0 6.6 6.6l2.2-2.2a1 1 0 0 1 1-.25 11.4 11.4 0 0 0 3.6.57 1 1 0 0 1 1 1V20a1 1 0 0 1-1 1A17 17 0 0 1 3 4a1 1 0 0 1 1-1h3.5a1 1 0 0 1 1 1c0 1.25.2 2.45.57 3.57a1 1 0 0 1-.25 1z" fill="#16233a"/></svg>
  </div>
  <div class="agent-label">TALK TO AN AGENT</div>
  <div class="agent-phone">888.888.8888</div>
</header>

<section class="hero" role="img" aria-label="Advisor reviewing market charts on a laptop over a city skyline"></section>
<h1 class="hero-title">Building Wealth.<b>Shaping Landscapes.</b></h1>
<p class="hero-copy">Perspiciatis unde omnis iste natus error sit voluptatem accusantium dolorem.</p>
<a class="btn-gold">GET STARTED</a>
<a class="btn-ghost">QUICK SUPPORT</a>
<span class="dot" style="left:122px"></span>
<span class="dot" style="left:145px"></span>
<span class="dot on" style="left:167px"></span>

<div class="wave"></div>
<div class="photo-a" role="img" aria-label="Site engineers on a construction project"></div>
<div class="photo-b" role="img" aria-label="Client shaking hands with an advisor"></div>
<h2 class="section-title about-title">About <b>Vayu Kiran Holdings</b></h2>
<div class="rule" style="left:603px;top:899px;width:117px"></div>
<p class="about-text lead">Faerspiciatis unde omnis istae natus error sitsec volupasctatem accusantium doloremque laudantium, totam reasscem aperiam, eaque ipsa quae ab illo inventore veritatis set quasi architecto beatae vitae dicta sunt explicabo. Nemo enim ipsam voluptatem quia voluptas sit aspernatur.</p>
<p class="about-text more">Heaed quia consequuntur magni dolores eos qui ratiase asefeeone voluptatem sequi nesciunt. Neque porro quisquam est, qui dolorem ipsum quia dolor sit amet, consectetur, adipisci velit, sed quia non numquam eius modi tempora incidunt ut labore et dolore magnam aliquam</p>
<a class="btn-learn">LEARN MORE</a>

<h2 class="section-title services-title">Our <b>Services</b></h2>
<div class="rule" style="left:542px;top:1436px;width:117px"></div>

<article class="card" style="left:147px">
  <svg width="70" height="70" viewBox="0 0 70 70" fill="none" stroke="#fff" stroke-width="2.5" stroke-linecap="round" stroke-linejoin="round">
    <path d="M6 34l16-14 10 8 22-20"/><path d="M44 8h10v10"/>
    <ellipse cx="14" cy="46" rx="9" ry="3.5"/><path d="M5 46v14c0 2 4 3.5 9 3.5s9-1.5 9-3.5V46M5 53c0 2 4 3.5 9 3.5s9-1.5 9-3.5"/>
    <ellipse cx="35" cy="40" rx="9" ry="3.5"/><path d="M26 40v20c0 2 4 3.5 9 3.5s9-1.5 9-3.5V40M26 47c0 2 4 3.5 9 3.5s9-1.5 9-3.5M26 54c0 2 4 3.5 9 3.5s9-1.5 9-3.5"/>
    <ellipse cx="56" cy="34" rx="9" ry="3.5"/><path d="M47 34v26c0 2 4 3.5 9 3.5s9-1.5 9-3.5V34M47 41c0 2 4 3.5 9 3.5s9-1.5 9-3.5M47 48c0 2 4 3.5 9 3.5s9-1.5 9-3.5M47 55c0 2 4 3.5 9 3.5s9-1.5 9-3.5"/>
  </svg>
  <h3>Investment</h3><span class="bar"></span>
  <p>Faeed quia consequuntur magni dolores eos qui ratione voluptatem sequi nesciunt. Neque porro quisquam esest, qui dolorem ipsum quia dolor siseft amet, consectetur, adipisci velit, sed quia non numquam eius modi tempora incidunt.</p>
</article>

<article class="card" style="left:465px">
  <svg width="76" height="76" viewBox="0 0 76 76" fill="none" stroke="#fff" stroke-width="2.5" stroke-linejoin="round">
    <rect x="3" y="36" width="68" height="36"/><path d="M3 48h68M3 60h68M20 36v12M40 36v12M60 36v12M12 48v12M30 48v12M50 48v12M20 60v12M40 60v12M60 60v12"/>
    <path d="M36 34l14-18 8 6-14 18z"/><path d="M56 18l12-14"/>
  </svg>
  <h3>Construction</h3><span class="bar"></span>
  <p>Faeed quia consequuntur magni dolores eos qui ratione voluptatem sequi nesciunt. Neque porro quisquam esest, qui dolorem ipsum quia dolor siseft amet, consectetur, adipisci velit, sed quia non numquam eius modi tempora incidunt.</p>
</article>

<article class="card feature" style="left:782px">
  <svg width="72" height="72" viewBox="0 0 72 72" fill="none" stroke="#16233a" stroke-width="3" stroke-linecap="round" stroke-linejoin="round">
    <rect x="6" y="6" width="60" height="60"/>
    <rect x="2" y="2" width="8" height="8" fill="#FFC000"/><rect x="62" y="2" width="8" height="8" fill="#FFC000"/>
    <rect x="2" y="62" width="8" height="8" fill="#FFC000"/><rect x="62" y="62" width="8" height="8" fill="#FFC000"/>
    <path d="M22 24l14 14 14-14M22 38l14 14 14-14" stroke-width="2.5" opacity="0"/>
    <path d="M24 36l8 8 16-16"/><path d="M36 18l18 18-18 18-18-18z"/>
  </svg>
  <h3>Land Sales</h3><span class="bar"></span>
  <p>Faeed quia consequuntur magni dolores eos qui ratione voluptatem sequi nesciunt. Neque porro quisquam esest, qui dolorem ipsum quia dolor siseft amet, consectetur, adipisci velit, sed quia non numquamincidunt.</p>
  <a class="more">Learn More</a>
</article>

<h2 class="section-title contact-title">Contact <b>Us</b></h2>
<div class="rule" style="left:542px;top:1989px;width:117px"></div>
<p class="contact-sub">Let’s Build Something Powerful Together</p>

<div class="landscape" role="img" aria-label="Countryside estate home with trees and lawn"></div>

<section class="contact-card">
  <h3 class="form-title">Send us a Message</h3>
  <svg class="abs" style="left:465px;top:22px" width="48" height="26" viewBox="0 0 48 26" fill="#f6d37a" stroke="#222" stroke-width="1.5">
    <rect x="14" y="3" width="32" height="20"/><path d="M14 3l16 11 16-11" fill="none"/><path d="M2 10h9M5 15h6M0 20h11" fill="none"/>
  </svg>
  <div class="field" style="left:21px;top:72px"><label>Your Name</label><span>Maya Ellison</span></div>
  <div class="field" style="left:272px;top:72px"><label>Email Address</label><span>info.mayaellison.com</span></div>
  <div class="field" style="left:21px;top:149px"><label>Phone</label><span>888 888 8888</span></div>
  <div class="field" style="left:272px;top:149px"><label>Company</label><span>Brightfield Company</span></div>
  <div class="field msg" style="left:21px;top:218px"><label>Enter Message</label><span>Hi, do you have a message to send?</span></div>
  <div class="send">
    <svg width="30" height="30" viewBox="0 0 24 24"><path d="M22 2L2 10l8 3 3 8z" fill="#fff"/><path d="M22 2L10 13" stroke="#222" stroke-width="1.5"/></svg>
  </div>

  <div class="info-panel">
    <h3 class="info-title">Contact Information</h3>
    <svg class="abs" style="left:296px;top:16px" width="38" height="38" viewBox="0 0 24 24"><path d="M3 11L12 3l9 8v10H3z" fill="#fff"/><circle cx="12" cy="13" r="3" fill="#3a7cc7"/></svg>
    <svg class="info-icon" style="top:80px" width="30" height="34" viewBox="0 0 24 28" fill="none" stroke="#fff" stroke-width="1.5"><path d="M2 10l6-3 8 3 6-3v18l-6 3-8-3-6 3z"/><path d="M12 4a4 4 0 0 1 4 4c0 3-4 7-4 7s-4-4-4-7a4 4 0 0 1 4-4z" fill="#3a7cc7"/></svg>
    <div class="info-row" style="top:78px">18 Harbourview Road, Northmead,<br>Australia</div>
    <svg class="info-icon" style="top:160px" width="30" height="28" viewBox="0 0 26 24" fill="none" stroke="#fff" stroke-width="1.5"><rect x="1" y="3" width="6" height="20"/><rect x="7" y="7" width="18" height="16"/><path d="M10 11h4M16 11h6M10 15h4M16 15h6M10 19h4M16 19h6"/></svg>
    <div class="info-row" style="top:161px">888.888.8888</div>
    <svg class="info-icon" style="top:224px" width="30" height="30" viewBox="0 0 24 24" fill="none" stroke="#fff" stroke-width="1.5"><path d="M2 10l10-7 10 7v12H2z"/><path d="M2 10l10 7 10-7"/><circle cx="12" cy="9" r="3"/></svg>
    <div class="info-row" style="top:226px">info@vayukiranholdings</div>
    <span class="social" style="left:30px"></span>
    <span class="social solid" style="left:73px"></span>
    <span class="social" style="left:116px"></span>
  </div>
</section>

<footer class="site-footer">
  <div class="footer-brand">VAYU KIRAN<span>HOLDINGS</span></div>
  <div class="fcol" style="left:488px"><h4>Quick links</h4><div class="bar"></div><a>Home</a><a>About</a><a>Services</a><a>Blog</a><a>Contact Us</a></div>
  <div class="fcol" style="left:698px"><h4>Links</h4><div class="bar"></div><a>Copyright</a><a>Legal</a><a>Privacy</a><a>Accessibility</a><a>Sitemap</a></div>
  <div class="fcol" style="left:887px"><h4>Support</h4><div class="bar"></div><a>FAQs</a><a>Privacy Policy</a><a>Terms of Service</a><a>Request a Quote</a><a>Client Login</a></div>
  <div class="footer-rule"></div>
  <p class="copy" style="left:111px">Copyright ©2025. All Rights Reserved</p>
  <a class="copy" style="left:861px">Terms of use</a>
  <a class="copy" style="left:971px">Privacy Policy</a>
  <svg class="abs" style="left:1130px;top:280px" width="18" height="46" viewBox="0 0 18 46" fill="none" stroke="#FFC000" stroke-width="2"><path d="M9 46V3M2 10l7-8 7 8"/></svg>
</footer>

</body>
</html>
```